Supply Chain Management Site - CrateLogix

We are a supply chain management company that offers the following products:
Warehouse Management System (WMS)
Order Management System (OMS)
Delivery / Fleet Management System

Our product caters to 3PL and distributions.

Ideally a site with a light background would be good.
We like the following sites:
www.venquor.com
http://www.brolvane.com/us/
http://www.tremvik.com/

You can use the content from here:
http://host.sample847.com/demo/crate-logix/

However, we really DO NOT like the design. You DO NOT have to have all the content on the home page. We can have the features and other things on other pages.

Some more content attached.

```html
<!DOCTYPE html>
<html lang="en">
<head>
<meta charset="utf-8">
<title>CrateLogix – Warehouse Management</title>
<link rel="stylesheet" href="https://fonts.googleapis.com/css2?family=Lato:wght@300&family=Open+Sans:ital,wght@0,300;0,400;1,400&display=swap">
<style>
:root{
  --teal:#6aa78d;
  --teal-light:#7cc0a0;
  --teal-dark:#5f9c82;
  --accent:#74bd9c;
  --ink:#2a2a2a;
  --rule:#d9d9d9;
  --panel:#f2f2f2;
  --white:#fff;
  --dot:#1aa98f;
}
*{margin:0;padding:0;box-sizing:border-box}
html,body{width:1200px;height:1000px;overflow:hidden;background:var(--white)}
body{font-family:"Open Sans",Arial,sans-serif;color:var(--ink);position:relative}

.site-header{position:absolute;left:0;top:0;width:1200px;height:85px;border-bottom:1px solid #e2e2e2}
.brand-name{position:absolute;left:161px;top:14px;font-family:"Lato",Arial,sans-serif;font-weight:300;font-size:44px;line-height:50px;color:#555;letter-spacing:.5px}
.main-nav{position:absolute;right:162px;top:39px;display:flex;font-size:12.5px}
.main-nav a{color:#222;text-decoration:none;margin-left:21px;display:flex;align-items:center;gap:3px}
.main-nav a.is-active{color:var(--accent)}
.main-nav .caret{font-size:7px;color:#999}

.hero{position:absolute;left:0;top:85px;width:1200px;height:352px;overflow:hidden;
  background:linear-gradient(90deg,var(--teal-light) 0%,#76b89a 15%,var(--teal-light) 25%,var(--teal-light) 100%)}
.hero-shade{position:absolute;inset:0}
.hero-title{position:absolute;left:174px;top:62px;font-size:38px;font-weight:300;color:var(--white);line-height:46px}
.hero-text{position:absolute;left:173px;top:113px;width:470px;font-size:18.5px;font-weight:300;line-height:28.5px;color:var(--white)}
.btn-more{position:absolute;left:174px;top:251px;width:96px;height:31px;font-size:16px;font-weight:300;color:#333;
  background:linear-gradient(#fafafa,#d2d2d2);border:1px solid #bbb;border-radius:2px;text-align:center;line-height:29px}
.hero-visual{position:absolute;left:705px;top:62px;width:272px;height:258px;border-radius:10px;
  background:linear-gradient(160deg,#c9a16a 0%,#b08753 60%,#9c7a4e 100%);opacity:.85}
.slider-dots{position:absolute;left:1008px;top:145px}

.intro{position:absolute;left:160px;top:466px;width:880px;text-align:center;border-bottom:1px solid var(--rule);padding-bottom:7px}
.intro h2{font-size:22.5px;font-weight:400;color:var(--ink);line-height:30px}

.features{position:absolute;left:160px;top:544px;width:880px;height:225px;display:flex}
.feature{position:relative;height:225px;text-align:center}
.feature + .feature{border-left:1px solid var(--rule)}
.feature:nth-child(1){width:290px}
.feature:nth-child(2){width:300px}
.feature:nth-child(3){width:290px}
.feature-icon{width:76px;height:76px;margin:2px auto 0;border-radius:8px}
.icon-strategy{background:radial-gradient(circle,#2b3a8a 0%,#9aa0b0 55%,rgba(255,255,255,0) 72%)}
.icon-planning{background:radial-gradient(circle,#f0dc8a 0%,#c9d6e6 50%,rgba(255,255,255,0) 72%)}
.icon-build{background:radial-gradient(circle,#e0b050 0%,#6b8fc4 45%,rgba(255,255,255,0) 72%)}
.feature h3{font-size:15.5px;font-weight:400;text-transform:uppercase;letter-spacing:.3px;margin-top:16px;line-height:20px}
.feature p{font-size:11px;line-height:15px;color:#222;width:236px;margin:9px auto 0;height:75px}
.feature:nth-child(2) p,.feature:nth-child(3) p{width:244px}
.know-more{position:absolute;left:0;right:0;top:207px;font-size:9px;color:#444;text-decoration:none;display:flex;justify-content:center;align-items:center;gap:5px}

.quality{position:absolute;left:159px;top:805px;width:882px;height:160px;background:var(--panel);border:1px solid #d6d6d6;text-align:center}
.quality h2{font-size:22.5px;font-weight:400;margin-top:18px;line-height:30px}
.quality p{font-size:12px;font-style:italic;line-height:18px;color:#333;width:790px;margin:27px auto 0}
</style>
</head>
<body>
<header class="site-header">
  <div class="brand-name">CrateLogix</div>
  <nav class="main-nav">
    <a class="is-active" href="#">Home</a>
    <a href="#">About us</a>
    <a href="#">Products <span class="caret">&#8964;</span></a>
    <a href="#">Features <span class="caret">&#8964;</span></a>
    <a href="#">Contact</a>
  </nav>
</header>

<section class="hero">
  <svg class="hero-shade" width="1200" height="352" aria-hidden="true">
    <polygon points="430,0 1200,0 1200,352 655,352" fill="var(--teal)"/>
  </svg>
  <h1 class="hero-title">Welcome To CrateLogix</h1>
  <p class="hero-text">Lorem Ipsum is simply dummy text of the printing and typesetting industry. Lorem Ipsum has been the indus-try's standard. of type and scrambled it to make a type specimen book.</p>
  <a class="btn-more">Read More</a>
  <div class="hero-visual" role="img" aria-label="Illustration of two warehouse workers beside a wrapped pallet of cardboard boxes"></div>
  <svg class="slider-dots" width="18" height="64" aria-hidden="true">
    <circle cx="8" cy="8" r="7" fill="var(--teal-dark)" stroke="#5a8f78"/>
    <circle cx="8" cy="31" r="7" fill="var(--dot)"/>
    <circle cx="8" cy="55" r="7" fill="var(--teal-dark)" stroke="#5a8f78"/>
  </svg>
</section>

<section class="intro">
  <h2>What a Warehouse Management System Should Be</h2>
</section>

<section class="features">
  <article class="feature">
    <div class="feature-icon icon-strategy" role="img" aria-label="Chess knight icon"></div>
    <h3>Strategy</h3>
    <p>Lorem Ipsum is simply dummy text of the printing and typesetting industry. Lorem Ipsum has been the industry's standard. of type and scrambled it to make a type</p>
    <a class="know-more" href="#">Know more <svg width="6" height="9" aria-hidden="true"><path d="M1 1l3.5 3.5L1 8" stroke="#222" stroke-width="2" fill="none"/></svg></a>
  </article>
  <article class="feature">
    <div class="feature-icon icon-planning" role="img" aria-label="Presentation easel icon"></div>
    <h3>Planning</h3>
    <p>System Integration &amp; Services is another Port-folio where we stand apart with a wide range of offering from Complex Hybrid Cloud Deployments to Emergency Server Support to Development and architectural</p>
    <a class="know-more" href="#">Know more <svg width="6" height="9" aria-hidden="true"><path d="M1 1l3.5 3.5L1 8" stroke="#222" stroke-width="2" fill="none"/></svg></a>
  </article>
  <article class="feature">
    <div class="feature-icon icon-build" role="img" aria-label="Charts with magnifying glass icon"></div>
    <h3>Build Our Work</h3>
    <p>It is a Leader in Technical Consultancy: Proven and we say that with pride. Clients approach us with Myriad of problems and achitecture help to Troubleshooting Critical Issues.Clients reach us from</p>
    <a class="know-more" href="#">Know more <svg width="6" height="9" aria-hidden="true"><path d="M1 1l3.5 3.5L1 8" stroke="#222" stroke-width="2" fill="none"/></svg></a>
  </article>
</section>

<section class="quality">
  <h2>Place Where Quality Matters...</h2>
  <p>Lorem Ipsum is simply dummy text of the printing and typesetting industry. Lorem Ipsum has been the industry's standard. of type and scrambled it to make a type specimen book.Lorem Ipsum is simply dummy text of the printing and typesetting industry. Lorem Ipsum has been the industry's standard. of type and scrambled it to make a type specimen book.</p>
</section>
</body>
</html>
```